1 Cohesive Design for all Tamberlin Steakhouse Menus

We have a general design that we like, labeled "Dinner Menu."
We are looking for the "Dinner Menu" to have a bit more character and for the other menus to mirror that design. The Dinner menu must remain 2 pages, side my side 8.5"x14". Headings must remain as are on the menu. Other menus attached are:
Brunch Menu: This is supplemental page for the Dinner Menu, must remain 1 page, 8.5"x14", we only need the content on the left side to be maintained.
Wine List: must remain double sided, headings remain the same, 11"x17"
Dessert List: must remain single sided, headings remain the same, 11"x4.25"
Cocktail Book: must be four 4.25"x11" pages, page 1 Wines by the glass, page 2 Draft and Bottled Beer, page 3 Classic Cocktails and Specialty Cocktails, page 4 Happy Hour, use "Cocktail Book" and "Proposed Happy Hour" attachments for content.
Color Scheme: Use color scheme in InDesign Files currently except make black text, true black.
We have also attached a photo with a box design idea that we like, "Box Idea," our entry way, dinner menu holder and cocktail book for inspiration. There are two InDesign file types, the newest 2014 version "Dinner" and an older file type "Dinner CS4," same with Brunch.

```html
<!DOCTYPE html>
<html lang="en">
<head>
<meta charset="utf-8">
<title>Tamberlin Steakhouse — Dinner Menu</title>
<link href="https://fonts.googleapis.com/css2?family=Josefin+Sans:wght@300;400&family=Work+Sans:ital,wght@0,600;0,700;1,600;1,700&family=Roboto+Slab:wght@400&display=swap" rel="stylesheet">
<style>
  :root{
    --red:#cf1f2e;
    --gold:#d4a12a;
    --gold-deep:#c39a3c;
    --ink:#000;
    --paper:#fff;
  }
  *{box-sizing:border-box;margin:0;padding:0}
  html,body{width:1200px;height:988px;overflow:hidden;background:var(--paper)}
  .menu{position:relative;width:1200px;height:988px;background:var(--paper);color:var(--ink);font-family:"Roboto Slab",serif}
  .page{position:absolute;top:0;height:988px;width:600px}
  .page--left{left:0}
  .page--right{left:600px}

  .section-head{position:absolute;display:flex;align-items:center;justify-content:center;gap:14px}
  .section-head .rule{flex:1;height:2px}
  .section-head .title{font-family:"Josefin Sans",sans-serif;font-weight:300;font-size:31px;letter-spacing:1px;white-space:nowrap;line-height:1}
  .section-head--gold .rule{background:var(--gold)}
  .section-head--gold .title{color:var(--gold)}
  .section-head--red .rule{background:var(--red)}
  .section-head--red .title{color:var(--red)}
  .flourish{display:inline-block;width:34px;height:10px;border-radius:6px;flex:none}
  .section-head--gold .flourish{background:var(--red)}
  .section-head--red .flourish{background:var(--red)}
  .divider-flourish{position:absolute;width:74px;height:9px;border-radius:6px;background:var(--red);opacity:.7}

  .item{position:absolute;text-align:center;line-height:1.12}
  .item .name{font-family:"Work Sans",sans-serif;font-weight:700;font-size:13.5px;color:var(--red);text-transform:uppercase}
  .item .price{color:var(--ink)}
  .item .desc{font-size:10.2px;color:var(--ink)}
  .item .sub{font-family:"Work Sans",sans-serif;font-weight:600;font-size:11px;text-transform:uppercase}

  .frame{position:absolute;border:2px solid var(--gold-deep);border-radius:14px}
  .frame::after{content:"";position:absolute;inset:4px;border:1px solid var(--gold-deep);border-radius:10px}

  .hq-title{position:absolute;left:45px;width:507px;text-align:center;font-family:"Work Sans",sans-serif;font-weight:700;font-size:21px;color:var(--red)}
  .hq-tag{position:absolute;left:45px;width:507px;text-align:center;font-family:"Work Sans",sans-serif;font-style:italic;font-weight:600;font-size:14px}

  .badge{position:absolute;left:900px;top:205px;width:240px;height:102px;background:var(--gold-deep);border-radius:18px;color:#fff;font-family:"Work Sans",sans-serif;font-weight:700}
  .badge .badge-name{position:absolute;left:16px;top:24px;font-size:27px;letter-spacing:.5px}
  .badge .badge-what{position:absolute;left:150px;top:22px;font-size:12.5px;line-height:1.4;text-align:center}
  .badge .badge-rule{position:absolute;left:16px;right:10px;top:62px;height:1px;background:#fff}
  .badge .badge-note{position:absolute;left:0;right:0;top:70px;text-align:center;font-style:italic;font-size:13px}

  .prime-box{position:absolute;left:657px;top:333px;width:514px;height:98px;border:3px dotted var(--red);border-radius:8px}
  .prime-title{position:absolute;left:688px;top:312px;padding:0 8px;background:var(--paper);font-family:"Josefin Sans",sans-serif;font-weight:300;font-size:28px;color:var(--red)}
  .prime-feat{position:absolute;left:868px;top:333px;font-family:"Work Sans",sans-serif;font-size:12px;font-weight:600}
  .prime-desc{position:absolute;left:680px;top:356px;width:460px;text-align:center;font-family:"Work Sans",sans-serif;font-style:italic;font-weight:600;font-size:11.3px;line-height:1.3;text-transform:uppercase}
  .cut{position:absolute;font-family:"Work Sans",sans-serif;font-weight:700;line-height:1.15}
  .cut .cut-name{color:var(--red);font-size:16px}
  .cut .cut-price{font-size:15px}

  .broiler-sub{position:absolute;left:660px;width:515px;top:493px;text-align:center;font-size:12px}
  .addons{position:absolute;left:960px;top:548px;width:180px;height:184px;background:var(--gold-deep);color:#fff;font-family:"Work Sans",sans-serif;text-align:center}
  .addons .addons-title{margin-top:16px;font-weight:700;font-size:13px}
  .addons .addons-rule{margin:6px 14px 10px;height:1px;background:#fff}
  .addons p{font-style:italic;font-weight:600;font-size:12.3px;line-height:1.15;margin-bottom:6px}
  .legend{position:absolute;left:683px;top:778px;font-family:"Work Sans",sans-serif;font-style:italic;font-weight:700;font-size:12px;color:var(--gold-deep)}

  .side{position:absolute;width:240px;text-align:center;font-family:"Work Sans",sans-serif;font-weight:700;font-size:11px;text-transform:uppercase}
</style>
</head>
<body>
<main class="menu">

  <!-- LEFT PAGE -->
  <section class="page page--left">
    <div class="section-head section-head--gold" style="left:12px;width:576px;top:48px">
      <span class="flourish" role="img" aria-label="scroll flourish"></span><span class="rule"></span>
      <span class="title">PRE–GAME</span>
      <span class="rule"></span><span class="flourish" role="img" aria-label="scroll flourish"></span>
    </div>

    <div class="item" style="left:20px;width:260px;top:100px">
      <div class="name">707º Drummies</div>
      <div class="sub">Drummies <span>$8.95</span> / 6 Drummies $14.95</div>
      <div class="desc">Tossed in 707º Hot Sauce, Honey Mustard or<br>Tamberlin BBQ, Blue Cheese Dip</div>
    </div>
    <div class="item" style="left:20px;width:260px;top:165px">
      <div class="name">Frickles <span class="price">$6.95</span></div>
      <div class="desc">Crispy Beer Batter Pickles, Chipotle Dip</div>
    </div>
    <div class="item" style="left:20px;width:260px;top:207px">
      <div class="name">Jalapeño Poppers <span class="price">$8.95</span></div>
      <div class="desc">Pimento Cheese, Chipotle Dip</div>
    </div>
    <div class="item" style="left:20px;width:260px;top:240px">
      <div class="name">Wisconsin Cheddar Curds</div>
      <div class="desc"><b style="font-family:'Work Sans',sans-serif;font-size:12px">$8.95</b> &nbsp; Beer Batter, Honey Mustard Dip</div>
    </div>

    <div class="item" style="left:300px;width:270px;top:102px">
      <div class="name">Cheesie Fat Fries <span class="price">$4.95</span></div>
      <div class="desc">Root Beer BBQ</div>
    </div>
    <div class="item" style="left:300px;width:270px;top:137px">
      <div class="name">Country Fried Chicken <span class="price">$9.95</span></div>
      <div class="desc">Chicken Thigs, Georgia Mustard</div>
    </div>
    <div class="item" style="left:300px;width:270px;top:172px">
      <div class="name">Flippin’ Nachos <span class="price">$10.95</span></div>
      <div class="desc">Crispy Corn Tortillas, Steakhouse Chili,<br>Nacho Cheese, Sour Cream, Scallions, Corn<br>Relish</div>
    </div>
    <div class="item" style="left:300px;width:270px;top:232px">
      <div class="name">Chips &amp; Salsa <span class="price">$6.95</span></div>
      <div class="desc">Charred Tomato Salsa, Tomatillo-Avocado</div>
    </div>

    <span class="divider-flourish" role="img" aria-label="scroll flourish" style="left:262px;top:287px"></span>

    <div class="section-head section-head--red" style="left:12px;width:576px;top:304px">
      <span class="flourish" role="img" aria-label="scroll flourish"></span><span class="rule"></span>
      <span class="title">BURGERS &amp; SANDWICHES</span>
      <span class="rule"></span><span class="flourish" role="img" aria-label="scroll flourish"></span>
    </div>

    <div class="item" style="left:20px;width:270px;top:353px">
      <div class="name">San Francisco Melt <span class="price">$14.95</span></div>
      <div class="desc">Sourdough, Cheddar, Swiss, Caramelized<br>Onion, Thick Cut Bacon, Not So Secret Sauce</div>
    </div>
    <div class="item" style="left:20px;width:270px;top:400px">
      <div class="name">Truffled ‘Shrooms<br>&amp; Swiss <span class="price">$14.95</span></div>
      <div class="desc">Roasted Mushrooms, Garlic, Caramelized<br>Onions, Swiss Cheese, Truffle Aioli</div>
    </div>
    <div class="item" style="left:20px;width:270px;top:458px">
      <div class="name">Western <span class="price">$14.95</span></div>
      <div class="desc">White Cheddar, Thick Cut Bacon, Onion<br>Rings, Root Beer Bbq Sauce</div>
    </div>
    <div class="item" style="left:20px;width:270px;top:504px">
      <div class="name">Marinated Portobello <span class="price">$12.95</span></div>
      <div class="desc">Local Goat Cheese, Roasted Peppers,<br>Lettuce, Onions, Not So Secret Sauce</div>
    </div>
    <div class="item" style="left:20px;width:270px;top:551px">
      <div class="name">Classic <span class="price">$10.95</span></div>
      <div class="desc">Lettuce, Onion, Pickle, Not So Secret Sauce</div>
    </div>

    <div class="item" style="left:305px;width:265px;top:353px">
      <div class="name">Ultimate Cheese <span class="price">$11.95</span></div>
      <div class="desc">Pepper Jack, Housemade American</div>
    </div>
    <div class="item" style="left:305px;width:265px;top:387px">
      <div class="name">Crispy Chicken <span class="price">$11.95</span></div>
      <div class="desc">707º Hot Sauce , Buttermilk Blue Cheese<br>Slaw</div>
    </div>
    <div class="item" style="left:305px;width:265px;top:434px">
      <div class="name">Carolina Pulled Pork <span class="price">$14.95</span></div>
      <div class="desc">Sweet &amp; Sour Cider Vinegar Slaw,<br>Honey Mustard BBQ</div>
    </div>
    <div class="item" style="left:305px;width:265px;top:481px">
      <div class="name">Tamberlin Philly <span class="price">$14.95</span></div>
      <div class="desc">Shaved Ribeye, Caramelized Onions,<br>Peppers, Provolone, Housemade American<br>Cheese</div>
    </div>

    <span class="divider-flourish" role="img" aria-label="scroll flourish" style="left:262px;top:595px"></span>

    <div class="section-head section-head--gold" style="left:12px;width:576px;top:612px">
      <span class="flourish" role="img" aria-label="scroll flourish"></span><span class="rule"></span>
      <span class="title">BIG PLATES</span>
      <span class="rule"></span><span class="flourish" role="img" aria-label="scroll flourish"></span>
    </div>

    <div class="item" style="left:20px;width:270px;top:656px">
      <div class="name">Cheese Steak Salad <span class="price">$15.95</span></div>
      <div class="desc">Peppers, Onions, Fried Potatoes, Cheesy<br>Ranch</div>
    </div>
    <div class="item" style="left:20px;width:270px;top:699px">
      <div class="name">Petaluma Brick Chicken <span class="price">$18.95</span></div>
      <div class="desc">Chili-Fennel Crusted, Bacon Mustard Jus,<br>3 Cabbage Slaw, Fat Fries</div>
    </div>
    <div class="item" style="left:305px;width:265px;top:656px">
      <div class="name">Old School Fish<br>and Chips <span class="price">$14.95</span></div>
      <div class="desc">Fried Thins, Lemons, Green Onion Tartar<br>Sauce, &nbsp; Malt Vinegar</div>
    </div>
    <div class="item" style="left:305px;width:265px;top:713px">
      <div class="name">Root Beer BBQ Ribs<br><span class="price">1/2 Rack $20.95 /<br>Full Rack $28.95</span></div>
      <div class="desc">Corn Muffin, 3 Cabbage Slaw, Fat Fries</div>
    </div>

    <div class="frame" style="left:45px;top:785px;width:507px;height:160px"></div>
    <div class="hq-title" style="top:803px">PRO FOOTBALL HEADQUARTERS</div>
    <div class="hq-tag" style="top:827px">— Every Team. Every Game. All the time —</div>

    <div class="item" style="left:60px;width:245px;top:857px">
      <div class="name">#TamberlinSuperfan</div>
      <div class="desc">Best dressed or most team spirit win prizes</div>
    </div>
    <div class="item" style="left:60px;width:245px;top:892px">
      <div class="name">Sat &amp; Sun Open @ 9:30AM</div>
      <div class="desc">Brunch served until 2pm</div>
    </div>
    <div class="item" style="left:300px;width:240px;top:857px">
      <div class="name">Pro Football Squares</div>
      <div class="desc">Monday Nights &amp; Harbor Hawks &amp; Bay Miners Games</div>
    </div>
    <div class="item" style="left:300px;width:240px;top:892px">
      <div class="name">Thursday Night Pick ‘Ems</div>
      <div class="desc">Winners every week</div>
    </div>
  </section>

  <!-- RIGHT PAGE -->
  <section class="page page--right">
    <div class="section-head section-head--red" style="left:20px;width:568px;top:48px">
      <span class="flourish" role="img" aria-label="scroll flourish"></span><span class="rule"></span>
      <span class="title">SIGNATURE STARTERS</span>
      <span class="rule"></span><span class="flourish" role="img" aria-label="scroll flourish"></span>
    </div>
  </section>

  <div class="item" style="left:650px;width:250px;top:97px">
    <div class="name">Classic Shrimp Louie <span class="price">$13.95</span></div>
    <div class="desc">Little Gem Lettuce, Avocado, Classic Louie<br>Dressing</div>
  </div>
  <div class="item" style="left:650px;width:250px;top:149px">
    <div class="name">Sonoma Garden <span class="price">$9.95</span></div>
    <div class="desc">Market Vegetables, Chardonnay Vinaigrette</div>
  </div>
  <div class="item" style="left:650px;width:250px;top:189px">
    <div class="name">Roasted Beets <span class="price">$9.95</span></div>
    <div class="desc">Soft Goat Cheese, Pistachio, Citrus<br>Vinaigrette</div>
  </div>
  <div class="item" style="left:650px;width:250px;top:241px">
    <div class="name">Classic Wedge <span class="price">$10.95</span></div>
    <div class="desc">Iceberg, Thick Cut Bacon, &nbsp;Tomato,<br>Red Onion, Blue Cheese-Ranch Dressing</div>
  </div>
  <div class="item" style="left:920px;width:240px;top:97px">
    <div class="name">Kale Caesar <span class="price">$9.95</span></div>
    <div class="desc">Roasted Garlic-Artichoke Dressing,<br>Parmesan,<br>Housemade Brown Butter Crouton</div>
  </div>
  <div class="item" style="left:920px;width:240px;top:161px">
    <div class="name">Mussels &amp; Frites <span class="price">$12.95</span></div>
    <div class="desc">White Wine, Garlic, Chili, Parsley</div>
  </div>

  <div class="badge">
    <span class="badge-name">ROCCO’S</span>
    <span class="badge-what">FAMOUS<br>POP-OVER</span>
    <span class="badge-rule"></span>
    <span class="badge-note">COMPLIMENTARY</span>
  </div>

  <div class="prime-box"></div>
  <div class="prime-title">PRIME RIB</div>
  <div class="prime-feat">Featuring Certified Heritage Beef ®</div>
  <div class="prime-desc">Signature rubbed and slow roasted served with a small iceberg wedge, salt baked potato, au jus, and creamy horseradish</div>
  <div class="cut" style="left:687px;top:390px"><div class="cut-name">STEAKHOUSE CUT 14OZ</div><div class="cut-price">$29.95</div></div>
  <div class="cut" style="left:920px;top:390px"><div class="cut-name">SPORTS BAR CUT 9OZ</div><div class="cut-price">$23.95</div></div>

  <div class="frame" style="left:660px;top:455px;width:515px;height:345px"></div>
  <div class="section-head section-head--gold" style="left:700px;width:435px;top:463px">
    <span class="rule" style="height:1px"></span>
    <span class="title" style="font-size:25px">FROM THE BROILER</span>
    <span class="rule" style="height:1px"></span>
  </div>
  <div class="broiler-sub">Our Steaks are served a la carte with our Signature Sea Salt-Peppercorn Rub</div>

  <div class="item" style="left:700px;width:230px;top:516px">
    <div class="name">Steak Frites au Poivre</div>
    <div class="name price">6oz $20.95 CHB®</div>
  </div>
  <div class="item" style="left:700px;width:230px;top:555px">
    <div class="name">NY Strip</div>
    <div class="name price">16oz $39.95 CHB®</div>
  </div>
  <div class="item" style="left:700px;width:230px;top:594px">
    <div class="name">Center Cut Filet</div>
    <div class="name price">8oz &nbsp;&nbsp;&nbsp; 12oz<br>$31.95 &nbsp; $35.95</div>
  </div>
  <div class="item" style="left:700px;width:230px;top:653px">
    <div class="name">Rib Eye</div>
    <div class="name price">16oz $34.95 CHB®</div>
  </div>
  <div class="item" style="left:690px;width:250px;top:695px">
    <div class="name">Double Cut Pork Chop <span class="price">$29.95</span></div>
    <div class="desc">Beer Brined, Seasonal Mostarda</div>
  </div>
  <div class="item" style="left:690px;width:250px;top:731px">
    <div class="name">Steakhouse Burger <span class="price">$19.95</span></div>
    <div class="desc">8oz Patty, Thick Cut Bacon, Aged White Cheddar,<br>Lettuce, Onions, Secret Sauce</div>
  </div>

  <div class="addons">
    <div class="addons-title">ADD ONS</div>
    <div class="addons-rule"></div>
    <p>MARYLAND LUMP<br>$14.95</p>
    <p>CRAB CAKE</p>
    <p>COLD WATER &nbsp;$19.95</p>
    <p>LOBSTER TAIL</p>
    <p>SWEET WATER &nbsp;$12.95<br>WHITE PRAWN</p>
  </div>
  <div class="legend">CHB® = Featuring Certified Heritage Beef ®</div>

  <div class="section-head section-head--red" style="left:622px;width:566px;top:840px">
    <span class="flourish" role="img" aria-label="scroll flourish"></span><span class="rule"></span>
    <span class="title" style="font-size:25px">STEAKHOUSE SIDES $5.95</span>
    <span class="rule"></span><span class="flourish" role="img" aria-label="scroll flourish"></span>
  </div>
  <div class="side" style="left:655px;top:883px">Creamed Spinach</div>
  <div class="side" style="left:655px;top:909px">Brussel Sprouts</div>
  <div class="side" style="left:655px;top:936px">Roasted Asparagus</div>
  <div class="side" style="left:905px;top:883px">Mushrooms a la Plancha</div>
  <div class="side" style="left:905px;top:909px">Classic Whipped Potatoes</div>
  <div class="side" style="left:905px;top:936px">Loaded Salt Baked Potato</div>

</main>
</body>
</html>
```